Website Design for BRAVO FREIGHTWAY

Hello. We are a Freight Brokage business in the transportation and logistics industry in the USA. Company name is BRAVO FREIGHTWAY. I'm looking to have a 5 page or less website built. Must have HOME, SHIPPERS, CARRIERS, ABOUT and CONTACT US.. I have additional information that needs to be placed in the footer of the website. Company address, contact info privacy and terms and conditions Need nice, vibrant looking site. The website needs to be a fully functionable site that is built and coded for wordpress and ready for hosting. Please visit these link for you to have an idea of the look and feel I want. www.tallowcargo.example www.pinecrest-haulage.example. Will have logo concept in 2 days for upload. As time goes by I will supply more content and the layout of the respective pages.

```html
<!DOCTYPE html>
<html lang="en">
<head>
<meta charset="utf-8">
<title>Bravo Freightway</title>
<link rel="stylesheet" href="https://fonts.googleapis.com/css2?family=Lato:wght@400;700&family=Titillium+Web:wght@400;600;700&display=swap">
<style>
:root{
  --ink:#1e1e1e;
  --panel:#2e2e2e;
  --panel-soft:#262626;
  --gold:#c69a00;
  --yellow:#f7c600;
  --white:#ffffff;
  --muted:#a9a9a9;
  --line:#3a3a3a;
  --backdrop:#cfcfcf;
}
*{box-sizing:border-box;margin:0;padding:0}
html,body{width:1200px;height:2942px;overflow:hidden;background:var(--backdrop)}
body{font-family:"Lato",sans-serif;color:var(--white)}
.site{position:absolute;left:145px;top:0;width:910px;height:2942px;background:var(--ink);overflow:hidden}
.abs{position:absolute}
.heading{font-family:"Titillium Web",sans-serif}
.brand{font-family:"Titillium Web",sans-serif;font-weight:600;font-size:13px;letter-spacing:.2px;display:flex;align-items:center;gap:7px;white-space:nowrap}
.brand-dot{width:10px;height:10px;background:var(--yellow)}
.hl{color:var(--yellow)}
.eyebrow{font-size:8px;letter-spacing:3px;color:var(--yellow);text-transform:uppercase}
.btn{position:absolute;display:flex;align-items:center;justify-content:center;font-size:8px;font-weight:700;text-transform:uppercase;white-space:nowrap}
.btn-outline{border:1px solid var(--yellow);color:var(--white)}
.btn-solid{background:var(--yellow);color:var(--white)}
.nav a{position:absolute;top:21px;font-size:8.5px;color:var(--white);text-decoration:none;text-transform:uppercase}
.header-rule{left:0;top:54px;width:910px;height:1px;background:var(--line)}
.hero-photo{left:0;top:55px;width:910px;height:423px;background:
  radial-gradient(ellipse 420px 200px at 240px 110px,rgba(198,154,0,.75),rgba(198,154,0,0) 70%),
  linear-gradient(180deg,#2a2a2a 0%,#262626 40%,#1e1e1e 100%)}
.truck{left:0;top:110px;width:480px;height:280px;background:linear-gradient(120deg,#e8e8e8 0%,#bcbcbc 40%,#2d3a5a 60%,#161c2c 100%);border-radius:4px;opacity:.9}
.hero-title{left:423px;top:166px;font-size:36px;line-height:36px;font-weight:600;white-space:nowrap}
.hero-sub{left:423px;top:295px;font-size:10px;white-space:nowrap}
.play{left:531px;top:333px;width:34px;height:34px;border:1.5px solid var(--yellow);border-radius:50%}
.benefits{left:22px;top:478px;width:864px;height:455px;background:var(--panel-soft)}
.cell{position:absolute;border-color:var(--line);border-style:solid;border-width:0}
.cell h4{font-family:"Lato",sans-serif;font-weight:700;font-size:10.5px;margin:12px 0 10px}
.cell p{font-size:8px;line-height:15.7px;color:var(--muted)}
.cell svg{display:block}
.benefit-title{left:124px;top:557px;font-size:22px;line-height:28px;font-weight:400}
.about-title{left:122px;top:1033px;font-size:26px;font-weight:700;white-space:nowrap}
.body-copy{font-size:10px;line-height:17px;color:#d4d4d4}
.body-copy b{color:var(--white)}
.rule{background:var(--line)}
.photo{border-radius:3px}
.stat{font-family:"Titillium Web",sans-serif;font-weight:600;font-size:12px;border-left:2px solid var(--yellow);padding-left:5px;line-height:12px;white-space:nowrap}
.process{left:22px;top:1444px;width:864px;height:201px;background:var(--yellow);overflow:hidden}
.process-title{left:100px;top:82px;font-size:26px;line-height:29px;font-weight:600;color:var(--ink)}
.card-label{font-size:7px;letter-spacing:1.5px;color:var(--yellow);text-transform:uppercase}
.card-title{font-family:"Titillium Web",sans-serif;font-weight:600;font-size:12px;text-transform:uppercase}
.contact{left:22px;top:2156px;width:864px;height:530px;background:var(--panel-soft)}
.field-label{font-size:7.5px;color:#e0e0e0}
.field-line{height:1px;background:var(--line)}
.footer-head{font-family:"Titillium Web",sans-serif;font-weight:600;font-size:11px;border-left:2px solid var(--yellow);padding-left:6px;line-height:11px}
.footer-list{font-size:8.5px;line-height:17px;color:var(--muted);white-space:nowrap}
.social{width:18px;height:18px;border:1px solid var(--yellow);border-radius:50%}
.legal{font-size:7px;color:var(--muted);white-space:nowrap}
</style>
</head>
<body>
<main class="site">

  <header>
    <div class="abs brand" style="left:84px;top:18px"><span class="brand-dot"></span>BRAVO FREIGHTWAY</div>
    <nav class="nav">
      <a style="left:524px">Home</a>
      <a style="left:582px">About</a>
      <a style="left:642px">Shippers</a>
      <a style="left:713px">Carriers</a>
    </nav>
    <div class="btn btn-outline" style="left:772px;top:12px;width:81px;height:30px">+ Contact Us</div>
    <div class="abs header-rule"></div>
  </header>

  <section>
    <div class="abs hero-photo" role="img" aria-label="Dusk landscape with golden hillside"></div>
    <div class="abs truck" role="img" aria-label="Semi truck with white trailer"></div>
    <h1 class="abs heading hero-title">Full truckload solutions<br>that help you <span class="hl">deliver</span> on<br>your promises<span class="hl">.</span></h1>
    <p class="abs hero-sub">Our extensive network of capacity stands ready to deliver your cargo on time!</p>
    <div class="btn btn-solid" style="left:423px;top:334px;width:98px;height:31px">+ Get a Free Quote</div>
    <div class="abs play"><svg width="31" height="31" viewBox="0 0 31 31"><path d="M12 10 L21 15.5 L12 21 Z" fill="var(--yellow)"/></svg></div>
  </section>

  <section>
    <div class="abs benefits"></div>
    <div class="cell" style="left:453px;top:478px;width:228px;height:228px;border-left-width:1px;border-bottom-width:1px"></div>
    <div class="cell" style="left:681px;top:478px;width:205px;height:228px;border-left-width:1px;border-bottom-width:1px"></div>
    <div class="cell" style="left:22px;top:706px;width:204px;height:227px;border-top-width:1px;border-right-width:1px"></div>
    <div class="cell" style="left:226px;top:706px;width:227px;height:227px;border-right-width:1px"></div>
    <div class="cell" style="left:453px;top:706px;width:228px;height:227px;border-right-width:1px"></div>

    <div class="abs eyebrow" style="left:124px;top:545px">Why choose us?</div>
    <h2 class="abs heading benefit-title">The Numerous Benefits<br>of Working With<br>Bravo Freightway</h2>

    <div class="cell" style="left:491px;top:540px;width:170px">
      <svg width="30" height="30" viewBox="0 0 30 30" fill="none" stroke="var(--yellow)" stroke-width="1.3"><rect x="3" y="10" width="14" height="17"/><rect x="17" y="14" width="10" height="13"/><path d="M6 14h3M11 14h3M6 18h3M11 18h3M6 22h3M11 22h3M8 10V4h6v6"/></svg>
      <h4>National &amp; Regional Capacity</h4>
      <p>Direct access to over 100 national,<br>regional, and local LTL carriers.</p>
    </div>
    <div class="cell" style="left:713px;top:540px;width:165px">
      <svg width="30" height="30" viewBox="0 0 30 30" fill="none" stroke="var(--yellow)" stroke-width="1.3"><path d="M5 16 L16 5 H26 V15 L15 26 Z"/><circle cx="21" cy="10" r="2"/><path d="M12 15h4M12 19h6"/></svg>
      <h4>Competitive Prices</h4>
      <p>We leverage our purchasing volume<br>to drive down costs.</p>
    </div>
    <div class="cell" style="left:52px;top:755px;width:165px">
      <svg width="30" height="30" viewBox="0 0 30 30" fill="none" stroke="var(--yellow)" stroke-width="1.3"><circle cx="15" cy="6" r="3"/><circle cx="7" cy="18" r="2.5"/><circle cx="15" cy="18" r="2.5"/><circle cx="23" cy="18" r="2.5"/><path d="M10 14h10M3 27c0-3 2-5 4-5s4 2 4 5M11 27c0-3 2-5 4-5s4 2 4 5M19 27c0-3 2-5 4-5s4 2 4 5"/></svg>
      <h4>Dedicated Representatives</h4>
      <p>A dedicated representative that<br>knows your business and can easily<br>troubleshoot shipment issues<br>without your involvement.</p>
    </div>
    <div class="cell" style="left:268px;top:755px;width:170px">
      <svg width="30" height="30" viewBox="0 0 30 30" fill="none" stroke="var(--yellow)" stroke-width="1.3"><path d="M10 4h17v11h-4l-3 3v-3H10z"/><path d="M3 10h5v9H6v3l-3-3z"/><path d="M14 9h1M18 9h1M22 9h1"/></svg>
      <h4>Proactive Communication</h4>
      <p>Proactive communication with<br>LTL carriers, problem resolutions,<br>and unparalleled knowledge of the<br>LTL landscape.</p>
    </div>
    <div class="cell" style="left:495px;top:755px;width:170px">
      <svg width="30" height="30" viewBox="0 0 30 30" fill="none" stroke="var(--yellow)" stroke-width="1.3"><rect x="6" y="3" width="14" height="20"/><path d="M9 8h8M9 12h8M9 16h5"/><rect x="14" y="16" width="12" height="10"/><path d="M17 21h6"/></svg>
      <h4>Billing Audits</h4>
      <p>Our team audits your shipments<br>before dispatching, to reduce your<br>chance of a rebill, due to inaccurate<br>or insufficient information.</p>
    </div>
    <div class="cell" style="left:713px;top:755px;width:170px">
      <svg width="30" height="30" viewBox="0 0 30 30" fill="none" stroke="var(--yellow)" stroke-width="1.3"><rect x="6" y="3" width="13" height="24" rx="2"/><rect x="12" y="10" width="14" height="7"/><path d="M14 13.5h1M18 13.5h1M22 13.5h1M11 24h3"/></svg>
      <h4>Accessorial Verification</h4>
      <p>Our teams provide verification of<br>shipper and receiver premises to<br>make sure your shipment doesn't<br>require any special considerations.</p>
    </div>
  </section>

  <section>
    <div class="abs eyebrow" style="left:122px;top:1021px">About us</div>
    <h2 class="abs heading about-title">Bravo Freightway Story</h2>
    <p class="abs body-copy" style="left:122px;top:1091px;width:340px">Bravo Freightway is a leading logistics company dedicated to providing innovative, efficient, and cost-effective logistics solutions to businesses of all sizes. <b>With a team of experienced professionals and cutting-edge technology,</b> we pride ourselves on our ability to streamline supply chain operations and ensure timely delivery.</p>
    <div class="abs rule" style="left:122px;top:1208px;width:357px;height:1px"></div>
    <p class="abs body-copy" style="left:122px;top:1238px;width:345px">Our commitment to <b>customer satisfaction is unparalleled,</b> and we work tirelessly to exceed our clients' expectations with every.</p>
    <div class="btn btn-outline" style="left:122px;top:1299px;width:80px;height:29px">+ Read More</div>
    <div class="abs rule" style="left:482px;top:1006px;width:1px;height:359px"></div>
    <div class="abs photo" style="left:520px;top:1002px;width:267px;height:324px;background:linear-gradient(135deg,#9a9a9a,#3c3c3c 60%,#6a6a6a)" role="img" aria-label="Two smiling truck drivers in front of trucks, black and white"></div>
    <div class="abs photo" style="left:676px;top:1205px;width:134px;height:95px;background:linear-gradient(135deg,#e2e2e2,#8a8a8a);border:2px solid #ffffff" role="img" aria-label="White semi truck on the road"></div>
    <div class="abs stat" style="left:520px;top:1350px">20+ Employees</div>
    <div class="abs stat" style="left:643px;top:1350px">15+ Years of Experience</div>
  </section>

  <section class="abs process">
    <div class="abs" style="left:330px;top:0;width:300px;height:201px;background:linear-gradient(90deg,rgba(247,198,0,0),rgba(90,88,80,.85) 45%,rgba(90,88,80,.85) 55%,rgba(247,198,0,0))" role="img" aria-label="Warehouse loading dock doors"></div>
    <div class="abs eyebrow" style="left:100px;top:65px;color:#d4a800">Our process</div>
    <h2 class="abs heading process-title">How We<br>Do It?</h2>
    <div class="btn" style="left:684px;top:69px;width:81px;height:28px;background:var(--ink)">+ Our Shippers</div>
    <div class="btn" style="left:684px;top:105px;width:81px;height:28px;border:1px solid var(--ink);color:var(--ink)">+ Our Carriers</div>
  </section>

  <section>
    <div class="abs photo" style="left:122px;top:1715px;width:267px;height:322px;background:linear-gradient(160deg,#d8d8d8,#6d6d6d 55%,#a8a8a8)" role="img" aria-label="Worker in a yellow hard hat among warehouse pallets, seen from above"></div>
    <div class="abs card-label" style="left:122px;top:2061px">What we do</div>
    <div class="abs card-title" style="left:122px;top:2076px">Freight Services</div>
    <div class="abs rule" style="left:426px;top:1715px;width:1px;height:368px"></div>
    <div class="abs photo" style="left:462px;top:1715px;width:154px;height:120px;background:linear-gradient(180deg,#bdbdbd,#6f6f6f 70%,#c9a100)" role="img" aria-label="Yellow forklift in a warehouse aisle"></div>
    <div class="abs photo" style="left:633px;top:1715px;width:154px;height:120px;background:linear-gradient(180deg,#a9a9a9,#5a5a5a 60%,#c9a100)" role="img" aria-label="Yellow forklift carrying goods"></div>
    <div class="abs card-label" style="left:462px;top:1860px">What we do</div>
    <div class="abs card-title" style="left:462px;top:1874px">FTL Freight</div>
    <div class="abs card-label" style="left:633px;top:1860px">What we do</div>
    <div class="abs card-title" style="left:633px;top:1874px">LTL Freight</div>
    <div class="abs rule" style="left:462px;top:1927px;width:325px;height:1px"></div>
    <p class="abs body-copy" style="left:462px;top:1961px;width:325px">We understand that businesses today face numerous challenges in managing their supply chains effectively. That's why Bravo Freightway offers a <b>range of customized freight solutions</b> tailored to meet the unique needs of each of our clients.</p>
    <p class="abs body-copy" style="left:462px;top:2041px;width:325px">Flexible &amp; scalable services ensure that our clients can quickly adapt to changing market conditions and stay ahead of the competition.</p>
  </section>

  <section>
    <div class="abs contact"></div>
    <div class="abs eyebrow" style="left:122px;top:2252px">Free quote</div>
    <h2 class="abs heading about-title" style="top:2263px">Get in Touch with Us</h2>
    <div class="abs field-label" style="left:122px;top:2320px">Full Name*</div>
    <div class="abs field-label" style="left:288px;top:2320px">Phone Number*</div>
    <div class="abs field-line" style="left:122px;top:2341px;width:153px"></div>
    <div class="abs field-line" style="left:288px;top:2341px;width:154px"></div>
    <div class="abs field-label" style="left:122px;top:2356px">Email Address*</div>
    <div class="abs field-label" style="left:288px;top:2356px">Shipper*</div>
    <div class="abs field-line" style="left:122px;top:2378px;width:153px"></div>
    <div class="abs field-line" style="left:288px;top:2378px;width:154px"></div>
    <div class="abs field-label" style="left:122px;top:2393px">City*</div>
    <div class="abs field-label" style="left:288px;top:2393px">State*</div>
    <div class="abs field-line" style="left:122px;top:2415px;width:153px"></div>
    <div class="abs field-line" style="left:288px;top:2415px;width:154px"></div>
    <div class="abs field-label" style="left:122px;top:2437px">How We Can Help*</div>
    <div class="abs field-line" style="left:122px;top:2515px;width:320px"></div>
    <div class="btn btn-solid" style="left:123px;top:2545px;width:107px;height:37px">+ Send Inquiry</div>
    <div class="abs" style="left:561px;top:2220px;width:226px;height:396px;background:radial-gradient(ellipse at 50% 50%,#2f2f2f,#262626 70%)" role="img" aria-label="Outline map of the service region with two office pins"></div>
  </section>

  <footer>
    <div class="abs brand" style="left:122px;top:2748px"><span class="brand-dot"></span>BRAVO FREIGHTWAY</div>
    <div class="abs social" style="left:123px;top:2793px"></div>
    <div class="abs social" style="left:147px;top:2793px"></div>

    <div class="abs footer-head" style="left:390px;top:2742px">Main Office</div>
    <p class="abs footer-list" style="left:390px;top:2769px">Bravo Freightway, LLC<br>410 N Harbor Rd<br>Suite 2180<br>Millbrook, WA 99045</p>
    <div class="abs footer-head" style="left:525px;top:2742px">Satellite Office</div>
    <p class="abs footer-list" style="left:525px;top:2769px">Satellite Office<br>7720 Linden Way<br>Suite 940<br>Eastport, WA 98190</p>
    <div class="abs footer-head" style="left:660px;top:2742px">Contact Info</div>
    <p class="abs footer-list" style="left:660px;top:2769px">1-888-555-0142<br>509-555-0187<br>509-555-0163<br>hello@bravofreightway.example</p>

    <div class="abs legal" style="left:390px;top:2912px;color:var(--yellow)">© 2023 Bravo Freightway</div>
    <div class="abs legal" style="left:659px;top:2912px">Privacy Policy &nbsp;|&nbsp; Terms and Conditions</div>
  </footer>

</main>
</body>
</html>
```